Web Design Project for Audio-Visual & Video Communications Business

We are currently busy with our new Wordpress website and require cutting-edge designs for our Home page. The intro images on the Home Page must give our visitors a quick overview of the services that we sell. These are broken down into 3 different services:

1. Audio-Visual (These include projectors, audio systems, projector screens, specialised brackets, Velmarc control systems, etc)

2. Video Communications products (We sell Tandivo and ClearNook equipment)

3. Online Shop (We need the best design to attract our existing and new visitors. The current design on the website was only done to show you what we have on offer)

We prefer to use the current theme but would like you to start building on top of this. This will be an ongoing project during 2013 to ensure that we keep the site fresh and updated.

Target Market(s)

We market our business to the Corporate, Education and Hospitality markets. We do however have individuals that will buy equipment online.

Industry/Entity Type

Building

Requirements
Must have
• The design must consist of 3 independent pages. We have several sliders that we can use on the Home page so you can decide if images and text must be visible at different times.
Nice to have
• You can visit the current draft website for the current look and feel. If you have completely new ideas we might consider them. Visit the site at www.linkvaro.co.za.

```html
<!DOCTYPE html>
<html lang="en">
<head>
<meta charset="utf-8">
<title>Linkvaro – Audio-Visual &amp; Video Communications</title>
<link href="https://fonts.googleapis.com/css2?family=Signika:wght@400;600&family=Arimo:wght@400&display=swap" rel="stylesheet">
<style>
:root{
  --green:#8fbc1e;
  --green-dark:#76a010;
  --charcoal:#5f5f66;
  --nav-dark:#3c3c3e;
  --page:#efefef;
  --text:#555;
  --heading:#444;
  --white:#fff;
  --footer-text:#f2f2f2;
}
*{margin:0;padding:0;box-sizing:border-box}
html,body{width:963px;height:1200px;overflow:hidden}
body{background:var(--page);font-family:"Arimo",Arial,sans-serif;color:var(--text);position:relative}
.abs{position:absolute}
.top-strip{left:0;top:0;width:963px;height:22px;background:var(--charcoal)}
.brand{left:96px;top:34px;display:flex;align-items:flex-end;gap:8px}
.brand-mark{width:40px;height:40px;border-radius:50%;background:var(--green);margin-bottom:4px}
.brand-name{font-family:"Signika",sans-serif;font-weight:600;font-size:26px;color:var(--green);line-height:1}
.util-links{right:96px;top:31px;display:flex;font-family:"Signika",sans-serif;font-size:9px;color:var(--green);text-transform:uppercase}
.util-links span{padding:0 8px;border-left:1px solid #ccc}
.util-links span:first-child{border-left:0}
.util-rule{left:612px;top:49px;width:255px;height:1px;background:#ddd}
.tagline{left:323px;top:71px;width:315px;height:43px;background:#f7f7f7;border:1px solid #e2e2e2;font-family:"Signika",sans-serif;font-size:10.5px;color:#333;display:flex;align-items:center;justify-content:center}
.cart{left:737px;top:71px;width:130px;height:43px;background:var(--green);color:var(--white);font-family:"Signika",sans-serif;font-size:14px;display:flex;align-items:center;justify-content:center;gap:8px}
.page-rule{left:0;top:176px;width:963px;height:3px;background:#dcdcdc}
.nav{left:96px;top:159px;width:556px;height:38px;background:linear-gradient(#59595c,#2f2f31);display:flex}
.nav a{font-family:"Signika",sans-serif;font-size:13px;color:var(--white);text-decoration:none;display:flex;align-items:center;justify-content:center;border-right:1px solid #2a2a2a;box-shadow:1px 0 0 #5e5e60}
.search{left:652px;top:159px;width:215px;height:38px;background:var(--green);padding:6px}
.search-field{width:100%;height:100%;background:#f4f4f4;border:1px solid #d4d4d4;position:relative}
.search-btn{position:absolute;right:0;top:0;width:27px;height:100%;border-left:1px solid #ddd}
.slider{left:96px;top:218px;width:771px;height:306px;background:#f3eeea;border:1px solid #e4e4e4;overflow:hidden}
.slide-title{left:8px;top:20px;width:420px;font-family:"Signika",sans-serif;font-size:14px;line-height:17px;color:#3a3a3a;text-transform:uppercase}
.slide-art{left:30px;top:68px;width:300px;height:210px;background:linear-gradient(135deg,#ece6e1,#e6dcd3)}
.slide-photo{left:420px;top:0;width:351px;height:306px;background:linear-gradient(100deg,#f3eeea 0,#e9d8c4 25%,#cfb28e 55%,#b89a78 75%,#a99b86 100%)}
.dots{left:14px;top:286px;display:flex;gap:9px}
.dots i{width:9px;height:9px;background:#ccc;display:block}
.dots i.on{background:#555}
.card{top:551px;width:241px;height:174px;background:var(--white);border:1px solid #e2e2e2;padding:4px}
.card-head{height:28px;background:var(--green);border-top-right-radius:14px;color:var(--white);font-family:"Signika",sans-serif;font-size:13.5px;display:flex;align-items:center;justify-content:space-between;padding:0 8px 0 12px}
.card-body{height:137px;background:linear-gradient(#f4f4f4,#e7e7e7)}
.card-img{width:100%;height:100%}
.product{position:relative;background:var(--white)}
.product-img{left:55px;top:12px;width:121px;height:88px;background:linear-gradient(#4d7fd0,#bcd6f2 70%,#555 71%,#222)}
.arrow-btn{top:54px}
.product-name{left:36px;top:112px;font-family:"Signika",sans-serif;font-size:14px;color:#333}
.product-price{left:134px;top:108px;font-family:"Signika",sans-serif;font-size:19px;color:var(--green)}
.welcome{left:98px;top:750px;font-family:"Signika",sans-serif;font-size:19px;color:var(--heading)}
.welcome-rule{left:96px;top:782px;width:771px;height:1px;background:#d8d8d8}
.intro{left:96px;top:800px;width:506px}
.intro .lead{font-size:11.3px;color:var(--green);margin-bottom:9px}
.intro p{font-size:9px;line-height:11.5px;text-align:justify;margin-bottom:11px}
.service{left:625px;width:241px;height:38px;background:var(--white);border:1px solid #e2e2e2;padding:3px}
.service div{height:100%;background:var(--green);color:var(--white);font-family:"Signika",sans-serif;font-size:13.5px;display:flex;align-items:center;gap:7px;padding-left:5px;text-transform:uppercase}
.footer{left:0;top:985px;width:963px;height:215px;background:var(--charcoal);color:var(--footer-text)}
.f-col{top:18px;font-size:9px}
.f-col h4{font-family:"Signika",sans-serif;font-weight:600;font-size:9px;text-transform:uppercase;margin-bottom:20px}
.f-col li{list-style:none;height:24px}
.f-col .mail{color:var(--green)}
.news-input{left:674px;top:44px;width:193px;height:26px;background:#f4f4f4}
.news-submit{left:794px;top:77px;width:73px;height:26px;background:var(--green);color:var(--white);font-family:"Signika",sans-serif;font-size:12px;display:flex;align-items:center;justify-content:center}
.social{left:687px;top:113px;display:flex;gap:14px}
.social i{display:block;width:22px;height:22px;border-radius:50%;background:#f0f0f0}
.f-rule{left:96px;top:168px;width:771px;height:1px;background:#7a7a80}
.copyright{left:0;top:188px;width:963px;text-align:center;font-size:9px}
</style>
</head>
<body>
<div class="abs top-strip"></div>

<header>
  <div class="abs brand"><span class="brand-mark"></span><span class="brand-name">Linkvaro</span></div>
  <nav class="abs util-links"><span>Shop</span><span>My Account</span><span>My Wishlist</span><span>Checkout</span></nav>
  <div class="abs util-rule"></div>
  <div class="abs tagline">LEADERS IN AUDIO-VISUAL AND VIDEO COMMUNICATIONS.</div>
  <div class="abs cart">
    <svg width="24" height="20" viewBox="0 0 24 20" fill="none" stroke="#fff" stroke-width="2"><path d="M1 2h4l3 11h12l2-8H7"/><circle cx="10" cy="17" r="1.6" fill="#fff"/><circle cx="18" cy="17" r="1.6" fill="#fff"/></svg>
    <span>MY CART &nbsp;(0)</span>
  </div>
</header>

<div class="abs page-rule"></div>
<nav class="abs nav">
  <a style="width:89px">HOME</a><a style="width:93px">SHOP</a><a style="width:113px">ABOUT US</a><a style="width:91px">BLOG</a><a style="width:170px;border-right:0;box-shadow:none;justify-content:flex-start;padding-left:29px">CONTACT US</a>
</nav>
<div class="abs search"><div class="search-field"><div class="search-btn">
  <svg width="27" height="24" viewBox="0 0 27 24" fill="none" stroke="#aaa" stroke-width="1.5"><circle cx="12" cy="11" r="4"/><path d="M15 14l5 4"/></svg>
</div></div></div>

<section class="abs slider">
  <h2 class="abs slide-title" style="font-weight:400">Linkvaro is the leading audio-visual &amp; video communications firm in South Africa.</h2>
  <div class="abs slide-art" role="img" aria-label="Illustration of online shopping icons: cart, delivery, payment, support and secure checkout"></div>
  <div class="abs slide-photo" role="img" aria-label="Photo of a customer paying online with a card at a laptop"></div>
  <div class="abs dots"><i class="on"></i><i></i><i></i></div>
</section>

<article class="abs card" style="left:96px">
  <div class="card-head">AUDIO VISUAL<svg width="15" height="15" viewBox="0 0 16 16"><circle cx="8" cy="8" r="8" fill="#fff"/><path d="M6.5 4.5L10 8l-3.5 3.5" stroke="#8fbc1e" stroke-width="2" fill="none"/></svg></div>
  <div class="card-body"><div class="card-img" role="img" aria-label="Laptop, projector, flat screen and media player" style="background:linear-gradient(110deg,#eee 0,#cfd8e0 30%,#555 50%,#c8a070 75%,#eee 100%)"></div></div>
</article>
<article class="abs card" style="left:362px">
  <div class="card-head">VIDEO COMMUNICATIONS<svg width="15" height="15" viewBox="0 0 16 16"><circle cx="8" cy="8" r="8" fill="#fff"/><path d="M6.5 4.5L10 8l-3.5 3.5" stroke="#8fbc1e" stroke-width="2" fill="none"/></svg></div>
  <div class="card-body"><div class="card-img" role="img" aria-label="Video call screens on monitor, tablet and phone" style="background:linear-gradient(#eee 0,#2b2b2b 15%,#5a6e80 50%,#222 85%,#eee 100%)"></div></div>
</article>
<article class="abs card" style="left:627px">
  <div class="card-head">ONLINE SHOPPING<svg width="15" height="15" viewBox="0 0 16 16"><circle cx="8" cy="8" r="8" fill="#fff"/><path d="M6.5 4.5L10 8l-3.5 3.5" stroke="#8fbc1e" stroke-width="2" fill="none"/></svg></div>
  <div class="card-body product">
    <div class="abs product-img" role="img" aria-label="Flat screen television product shot"></div>
    <svg class="abs arrow-btn" style="left:8px" width="16" height="16" viewBox="0 0 16 16"><circle cx="8" cy="8" r="8" fill="#555"/><path d="M9.5 4.5L6 8l3.5 3.5" stroke="#fff" stroke-width="2" fill="none"/></svg>
    <svg class="abs arrow-btn" style="left:212px" width="16" height="16" viewBox="0 0 16 16"><circle cx="8" cy="8" r="8" fill="#555"/><path d="M6.5 4.5L10 8l-3.5 3.5" stroke="#fff" stroke-width="2" fill="none"/></svg>
    <span class="abs product-name">NUVARO VISTA</span>
    <span class="abs product-price">$328.00</span>
  </div>
</article>

<h1 class="abs welcome" style="font-weight:400">Welcome to Linkvaro.</h1>
<div class="abs welcome-rule"></div>
<section class="abs intro">
  <p class="lead">Linkvaro is the leading Audio-Visual &amp; Video Communications firm in South Africa.</p>
  <p>Our team comes with more than 16 years experience in the Corporate, Education &amp; Hospitality markets. The main reason why we founded Linkvaro was to consult to companies and individuals on an independent basis, and to ensure that the best solutions are specified before selecting an AV Integration company to install their Audio-Visual or Video Communications solutions.</p>
  <p>During the past few years we have experienced installations from different Audio-Visual Integration companies in South Africa that is not on the correct standard. Even though all these companies had access to the same products and training they all managed to install the equipment in a different way, and most of the time not focussing on the user experience.</p>
  <p>The main focus at Linkvaro is to ensure that our selected customers can choice between different suppliers without compromising on quality.</p>
</section>

<div class="abs service" style="top:796px"><div><svg width="15" height="15" viewBox="0 0 16 16"><circle cx="8" cy="8" r="8" fill="#fff"/><path d="M6.5 4.5L10 8l-3.5 3.5" stroke="#8fbc1e" stroke-width="2" fill="none"/></svg>Consultation &amp; Design</div></div>
<div class="abs service" style="top:840px"><div><svg width="15" height="15" viewBox="0 0 16 16"><circle cx="8" cy="8" r="8" fill="#fff"/><path d="M6.5 4.5L10 8l-3.5 3.5" stroke="#8fbc1e" stroke-width="2" fill="none"/></svg>Project Management</div></div>
<div class="abs service" style="top:884px"><div><svg width="15" height="15" viewBox="0 0 16 16"><circle cx="8" cy="8" r="8" fill="#fff"/><path d="M6.5 4.5L10 8l-3.5 3.5" stroke="#8fbc1e" stroke-width="2" fill="none"/></svg>Supply &amp; Installation</div></div>
<div class="abs service" style="top:929px"><div><svg width="15" height="15" viewBox="0 0 16 16"><circle cx="8" cy="8" r="8" fill="#fff"/><path d="M6.5 4.5L10 8l-3.5 3.5" stroke="#8fbc1e" stroke-width="2" fill="none"/></svg>Onsite Support Personal</div></div>

<footer class="abs footer">
  <div class="abs f-col" style="left:104px"><h4>Information</h4><ul><li>Home</li><li>Shop</li><li>About us</li><li>Blog</li><li>Contact us</li></ul></div>
  <div class="abs f-col" style="left:290px"><h4>My Account</h4><ul><li>My Account</li><li>My Wishlist</li><li>Checkout</li><li>Faq</li><li>Help</li></ul></div>
  <div class="abs f-col" style="left:481px"><h4>Contact Info</h4><ul><li>Phone: +27 21 555-0142</li><li class="mail">Email: info@linkvaro.co.za</li></ul><p style="line-height:14.5px;margin-top:5px">The Arcade, Harbour Park,<br>Cape Town, South Africa,<br>7400</p></div>
  <div class="abs f-col" style="left:675px"><h4>Sing up for newsletter</h4></div>
  <div class="abs news-input"></div>
  <div class="abs news-submit">SUBMIT</div>
  <div class="abs social" aria-label="Social links"><i></i><i></i><i></i><i></i><i></i></div>
  <div class="abs f-rule"></div>
  <p class="abs copyright">Copyright 2013 Linkvaro (Pty) Ltd. | All Rights Reserved | Leaders in Audio-Visual &amp; Video Communications.</p>
</footer>
</body>
</html>
```